Business Card Design with new logo

Dorian Pelleway 4172
E 118th St Dunmere, IL 62951
Cell: 217-555-0193
pellewayrestoration@mailvane.test

Classic Car Restoration Services Buy Sell Trade Consign

Dorian Pelleway 9698
Cell: 217-555-0193

```html
<!DOCTYPE html>
<html lang="en">
<head>
<meta charset="utf-8">
<title>Pelleway Restoration LLC – Business Card</title>
<link rel="stylesheet" href="https://fonts.googleapis.com/css2?family=Lato:ital,wght@0,400;0,700;0,900;1,700&family=Oswald:wght@500&display=swap">
<style>
  :root {
    --brand-red: #b71f24;
    --bright-red: #e8302c;
    --ink: #17242e;
    --paper: #ffffff;
    --stage: #ececec;
    --muted: #333333;
  }
  * { box-sizing: border-box; margin: 0; padding: 0; }
  html, body { width: 1200px; height: 586px; overflow: hidden; }
  body { background: var(--stage); font-family: "Lato", sans-serif; position: relative; }

  .card { position: absolute; top: 129px; width: 501px; height: 300px; overflow: hidden; }
  .card-front { left: 62px; background: var(--brand-red); color: var(--paper); }
  .card-back { left: 619px; background: var(--paper); }

  .brand { position: absolute; left: 0; right: 0; text-align: center; }
  .brand-dot { display: block; margin: 0 auto; border-radius: 50%; }
  .brand-name { display: block; font-family: "Lato", sans-serif; font-weight: 900; text-transform: uppercase; line-height: 1; }
  .brand-sub { display: block; font-family: "Lato", sans-serif; font-weight: 900; text-transform: uppercase; line-height: 1; }

  .card-front .brand { top: 56px; }
  .card-front .brand-dot { width: 64px; height: 64px; background: var(--paper); margin-bottom: 26px; }
  .card-front .brand-name { font-size: 38px; letter-spacing: 3px; color: var(--paper); }
  .card-front .brand-sub { font-size: 14px; letter-spacing: 10px; margin-top: 9px; color: var(--paper); }

  .tagline { position: absolute; left: 0; right: 0; top: 256px; text-align: center; font-size: 13px; font-weight: 700; font-style: italic; letter-spacing: 0.3px; }

  .card-back .brand { top: 34px; }
  .card-back .brand-dot { width: 48px; height: 48px; background: var(--bright-red); margin-bottom: 18px; }
  .card-back .brand-name { font-size: 27px; letter-spacing: 2px; color: var(--ink); }
  .card-back .brand-sub { font-size: 11px; letter-spacing: 7px; margin-top: 7px; color: var(--brand-red); }

  .person { position: absolute; right: 286px; top: 197px; text-align: right; }
  .person-name { font-family: "Oswald", sans-serif; font-weight: 500; font-size: 17px; color: var(--brand-red); text-transform: uppercase; letter-spacing: 0.5px; line-height: 1.1; }
  .person-role { font-size: 11px; color: var(--muted); margin-top: 1px; }
  .person-address { font-size: 12px; font-weight: 700; color: var(--brand-red); margin-top: 10px; white-space: nowrap; }

  .divider { position: absolute; left: 240px; top: 187px; width: 2px; height: 76px; background: linear-gradient(to bottom, transparent, var(--bright-red), transparent); }

  .contacts { position: absolute; left: 268px; top: 204px; list-style: none; }
  .contacts li { display: flex; align-items: center; height: 24px; font-size: 11.5px; color: #111; white-space: nowrap; }
  .contact-icon { width: 18px; height: 18px; border-radius: 50%; background: var(--brand-red); margin-right: 9px; flex: none; display: flex; align-items: center; justify-content: center; }

  .footer-band { position: absolute; bottom: 0; height: 10px; }
  .footer-band-light { left: 0; width: 251px; background: var(--bright-red); }
  .footer-band-dark { left: 251px; right: 0; background: var(--brand-red); }
</style>
</head>
<body>
  <section class="card card-front">
    <div class="brand">
      <span class="brand-dot"></span>
      <span class="brand-name">Pelleway</span>
      <span class="brand-sub">Restoration LLC</span>
    </div>
    <p class="tagline">Classic Car Restoration Services Buy Sell Trade Consign</p>
  </section>

  <section class="card card-back">
    <div class="brand">
      <span class="brand-dot"></span>
      <span class="brand-name">Pelleway</span>
      <span class="brand-sub">Restoration LLC</span>
    </div>

    <div class="person">
      <p class="person-name">Dorian Pelleway</p>
      <p class="person-role">Redline Advisors</p>
      <p class="person-address">4172 E 118th St Dunmere, IL 62951</p>
    </div>

    <div class="divider"></div>

    <ul class="contacts">
      <li>
        <span class="contact-icon">
          <svg width="10" height="10" viewBox="0 0 24 24" aria-hidden="true"><path fill="#fff" d="M6.6 10.8a15.1 15.1 0 0 0 6.6 6.6l2.2-2.2c.3-.3.7-.4 1-.2 1.1.4 2.3.6 3.6.6.6 0 1 .4 1 1V20c0 .6-.4 1-1 1A17 17 0 0 1 3 4c0-.6.4-1 1-1h3.5c.6 0 1 .4 1 1 0 1.3.2 2.5.6 3.6.1.3 0 .7-.2 1z"/></svg>
        </span>
        217-555-0193
      </li>
      <li>
        <span class="contact-icon">
          <svg width="10" height="10" viewBox="0 0 24 24" aria-hidden="true"><path fill="#fff" d="M2 5h20v14H2z"/><path fill="none" stroke="#b71f24" stroke-width="2" d="M2 5l10 8 10-8"/></svg>
        </span>
        pellewayrestoration@mailvane.test
      </li>
    </ul>

    <div class="footer-band footer-band-light"></div>
    <div class="footer-band footer-band-dark"></div>
  </section>
</body>
</html>
```